Design signage for shop front glass windows

Our clinic is called Marrowind Medical Practice and we are a general practice offering medical services. Our services include
1. General Practice Consultations
2. Immunisations
3. Health checks
4. Women's health
5. Men's Health
6. Skin cancer checks
7. Travel medicine
8. Referrals
9. Antenatal checks
10. Minor surgery
11. Cosmetic medicine
12. Pre Employment Medicals
13. Diabetes care
14. Wound care
and much more

Our motto is
"friendly and professional health care for you and your family"

We also have a range of allied health services
including
Psychology
Physiotherapy
Podiatry
Dietetics and Nutrition
Exercise Physiology
Diabetes Education

On the signs there should be the words "Bulk Billing for GP services'
"Book online at www.marrowindmedicalpractice.example.au"
"Ph: 07 3190 4286"

We have glass windows on our shopfront - there are 11 panels (see attached photos) - 3 panels on the left have a white film and 4 panels in the centre are just tinted (no further signage will be installed on the central glass doors which are not included). There are another 4 panels on the right that have a white film. We are looking for a design for the glass signage to promote our services. We will print signage that can be stuck on the glass. There will need to be more bold signage on the white film and more subtle minor signage on the tinted glass windows which can still allow light thru. I have attached pictures of the window. Our logo is on our website www.marrowindmedicalpractice.example.au to get an idea of colours.

Target Market(s)

Young families living in the region of Capalaba Queensland

Industry/Entity Type

Health Care

Font styles to use
Serif

Colors
85abd2
acd036
ec1f27

Requirements
Must have
• The words
• "Bulk Billing for General Practice Services"
• "friendly and professional health care for you and your family"
• Book online at www.marrowindmedicalpractice.example.au
• Phone 07 3190 4286

```html
<!DOCTYPE html>
<html lang="en">
<head>
<meta charset="utf-8">
<title>Marrowind Medical Practice – Window Signage</title>
<link rel="stylesheet" href="https://fonts.googleapis.com/css2?family=Dosis:wght@400;500;600&family=PT+Sans+Narrow&display=swap">
<style>
  :root {
    --bg: #eceef0;
    --white: #ffffff;
    --brand-green: #1f9a3c;
    --brand-red: #e0262d;
    --brand-blue: #2a7fc1;
    --ink: #2b2b2b;
    --band-blue: #1f78c4;
    --band-green: #1a9a45;
  }
  * { box-sizing: border-box; margin: 0; padding: 0; }
  html, body { width: 1200px; height: 900px; overflow: hidden; background: var(--bg); }
  .signage {
    display: flex; gap: 20px;
    padding: 80px 30px;
    width: 1200px; height: 900px;
  }
  .panel {
    position: relative;
    flex: 1 1 0;
    height: 740px;
    background: var(--white);
    box-shadow: 0 2px 10px rgba(0,0,0,0.12);
    display: flex; flex-direction: column;
    overflow: hidden;
    font-family: "Dosis", sans-serif;
  }
  .panel__header { padding: 26px 22px 0; height: 290px; }
  .brand {
    display: flex; align-items: center; gap: 8px;
    color: var(--brand-green);
    font-family: "Dosis", sans-serif;
    font-weight: 600; font-size: 17px; line-height: 1.1;
  }
  .brand__mark { width: 12px; height: 12px; background: var(--brand-green); flex: none; }
  .service { margin-top: 44px; color: var(--brand-red); }
  .service__kicker { font-size: 18px; font-weight: 400; }
  .service__title { font-size: 34px; font-weight: 500; line-height: 1; }
  .service__text {
    margin-top: 10px;
    color: var(--brand-blue);
    font-family: "PT Sans Narrow", sans-serif;
    font-size: 14px; line-height: 1.25;
  }
  .dial {
    margin-top: 18px;
    color: var(--ink);
    font-family: "PT Sans Narrow", sans-serif;
    font-size: 17px;
  }
  .photo { flex: 1; }
  .photo--exercise { background: linear-gradient(160deg, #c9d3dc, #8b96a1 60%, #6f7a84); }
  .photo--diabetes { background: linear-gradient(160deg, #f4e3d8, #e8c6b2 55%, #f6f1ee); }
  .photo--physio { background: linear-gradient(160deg, #eef0f2, #d9b59c 55%, #b9c3cc); }
  .photo--podiatry { background: linear-gradient(160deg, #f3f4f6, #e2c4ae 55%, #dfe3e7); }
  .band {
    height: 140px;
    background: linear-gradient(100deg, var(--band-blue) 0%, var(--band-blue) 35%, var(--band-green) 100%);
    color: var(--white);
    padding: 26px 22px 0;
    font-family: "PT Sans Narrow", sans-serif;
  }
  .band__billing { font-size: 19px; }
  .band__book { margin-top: 12px; font-size: 13px; line-height: 1.3; }
</style>
</head>
<body>
<main class="signage">

  <section class="panel">
    <div class="panel__header">
      <div class="brand"><span class="brand__mark"></span>Marrowind Medical Practice</div>
      <div class="service">
        <div class="service__kicker">Exercise</div>
        <h2 class="service__title">Physiology</h2>
      </div>
      <p class="service__text">Customized exercise programs to meet health care needs</p>
      <p class="dial">Dial Now: 07 3190 4286</p>
    </div>
    <div class="photo photo--exercise" role="img" aria-label="Man doing push-ups in an exercise studio"></div>
    <div class="band">
      <p class="band__billing">Bulk Billing for GP services</p>
      <p class="band__book">Book online at<br>www.marrowindmedicalpractice.example.au</p>
    </div>
  </section>

  <section class="panel">
    <div class="panel__header">
      <div class="brand"><span class="brand__mark"></span>Marrowind Medical Practice</div>
      <div class="service">
        <div class="service__kicker">Managing</div>
        <h2 class="service__title">Diabetes</h2>
      </div>
      <p class="service__text">It's not easy, but it's worth it. Marrowind helps you take that step</p>
      <p class="dial">Dial Now: 07 3190 4286</p>
    </div>
    <div class="photo photo--diabetes" role="img" aria-label="Hands using a blood glucose meter on a fingertip"></div>
    <div class="band">
      <p class="band__billing">Bulk Billing for GP services</p>
      <p class="band__book">Book online at<br>www.marrowindmedicalpractice.example.au</p>
    </div>
  </section>

  <section class="panel">
    <div class="panel__header">
      <div class="brand"><span class="brand__mark"></span>Marrowind Medical Practice</div>
      <div class="service">
        <div class="service__kicker">Pure</div>
        <h2 class="service__title">Physiotherapy</h2>
      </div>
      <p class="service__text">We offer the highest quality assessment, diagnosis and treatment</p>
      <p class="dial">Dial Now: 07 3190 4286</p>
    </div>
    <div class="photo photo--physio" role="img" aria-label="Physiotherapist examining a patient's knee"></div>
    <div class="band">
      <p class="band__billing">Bulk Billing for GP services</p>
      <p class="band__book">Book online at<br>www.marrowindmedicalpractice.example.au</p>
    </div>
  </section>

  <section class="panel">
    <div class="panel__header">
      <div class="brand"><span class="brand__mark"></span>Marrowind Medical Practice</div>
      <div class="service">
        <div class="service__kicker">Premier</div>
        <h2 class="service__title">Podiatrics</h2>
      </div>
      <p class="service__text">We provide experienced and expert podiatry services.</p>
      <p class="dial">Dial Now: 07 3190 4286</p>
    </div>
    <div class="photo photo--podiatry" role="img" aria-label="Gloved hand examining a patient's foot"></div>
    <div class="band">
      <p class="band__billing">Bulk Billing for GP services</p>
      <p class="band__book">Book online at<br>www.marrowindmedicalpractice.example.au</p>
    </div>
  </section>

</main>
</body>
</html>
```